Corvane Holdings , new business card design

investment firm with corporate clients . need double sided business card , vertical and horizontal options ,logo must be clear. prefer pantone colors only and sharp design. website also www.corvane-example.ae

Khalid Bin Rashed
Managing Director
Tel. +971 4 000 3829
Mobile +971 50 000 4172
khalid@corvane-example.ae
Palm Crest Tower, officw 18-B07, Qasr Gardens, Dubai

Contact Information for Business Card

Khalid Bin Rashed
Managing Director

Font styles to use
Serif

Colors

Designer to choose colors to be used in the design.

```html
<!DOCTYPE html>
<html lang="en">
<head>
<meta charset="utf-8">
<title>Corvane Holdings – Business Card 50 x 90 Vertical</title>
<link href="https://fonts.googleapis.com/css2?family=Jost:ital,wght@0,300;0,400;0,600;1,400&display=swap" rel="stylesheet">
<style>
  :root {
    --board-light: #f4f4f4;
    --board-mid: #d2d2d2;
    --board-dark: #a9a9a9;
    --card-white: #ffffff;
    --panel-grey: #4a4a4a;
    --panel-rule: #3a3a3a;
    --panel-rule-light: #5e5e5e;
    --ink: #1c1c1c;
    --ink-soft: #6a6a6a;
    --on-dark: #f2f2f2;
    --accent-blue: #3a7cc4;
  }
  * { box-sizing: border-box; margin: 0; padding: 0; }
  html, body { width: 1200px; height: 1114px; overflow: hidden; }
  body {
    position: relative;
    font-family: "Jost", sans-serif;
    color: var(--ink);
    background: radial-gradient(ellipse at 50% 45%, var(--board-light) 0%, var(--board-mid) 60%, var(--board-dark) 100%);
  }
  .board-title {
    position: absolute; top: 62px; left: 0; width: 1200px;
    text-align: center; font-size: 31px; font-weight: 400; color: #111;
  }
  .side-label {
    position: absolute; top: 136px; width: 200px; text-align: center;
    font-size: 25px; font-weight: 400; color: #111;
  }
  .side-label--front { left: 272px; }
  .side-label--back { left: 775px; }

  .card {
    position: absolute; background: var(--card-white);
    box-shadow: 6px 7px 6px rgba(0,0,0,.35);
    border: 1px solid #9a9a9a;
  }
  .card--front { left: 140px; top: 175px; width: 460px; height: 828px; overflow: hidden; }
  .card--back { left: 643px; top: 177px; width: 459px; height: 826px; }

  .brand {
    position: absolute; left: 0; width: 100%;
    text-align: center; color: var(--ink); font-weight: 300;
  }
  .brand__name { display: block; font-size: 50px; letter-spacing: 14px; line-height: 1; padding-left: 14px; }
  .brand__sub { display: block; font-size: 19px; letter-spacing: 15px; margin-top: 10px; padding-left: 15px; }
  .brand--front { top: 50px; }
  .brand--back { top: 694px; }

  .tagline {
    position: absolute; top: 206px; width: 100%; text-align: center;
    font-size: 32px; font-weight: 400; color: var(--ink-soft);
  }
  .services {
    position: absolute; top: 322px; width: 100%; text-align: center;
    font-size: 26px; font-style: italic; color: #1a1a1a;
  }

  .contact-panel {
    position: absolute; left: 0; top: 350px; width: 460px; height: 478px;
    background: var(--panel-grey); color: var(--on-dark);
  }
  .contact-panel__spine {
    position: absolute; left: 81px; top: 0; width: 2px; height: 100%;
    background: var(--panel-rule); border-right: 1px solid var(--panel-rule-light);
  }
  .icon { position: absolute; left: 23px; width: 40px; height: 40px; fill: var(--on-dark); }
  .contact-line {
    position: absolute; left: 88px; width: 360px; text-align: center;
    font-size: 23px; font-weight: 400; line-height: 1.2; white-space: nowrap;
  }
  .contact-line strong { font-weight: 600; }
  .contact-line--small { font-size: 22px; }
  .rule {
    position: absolute; left: 96px; width: 342px; height: 2px;
    background: var(--panel-rule); border-bottom: 1px solid var(--panel-rule-light);
  }
</style>
</head>
<body>
  <h1 class="board-title">50 X 90 Vertical</h1>
  <p class="side-label side-label--front">Front</p>
  <p class="side-label side-label--back">Back</p>

  <section class="card card--front" aria-label="Card front">
    <div class="brand brand--front">
      <span class="brand__name">CORVANE</span>
      <span class="brand__sub">HOLDINGS</span>
    </div>
    <p class="tagline">Tag Line Here</p>

    <div class="contact-panel">
      <div class="contact-panel__spine"></div>

      <svg class="icon" style="top:36px" viewBox="0 0 40 40" aria-hidden="true">
        <circle cx="20" cy="11" r="9"/>
        <path d="M4 38 C4 26 10 22 20 22 C30 22 36 26 36 38 Z"/>
      </svg>
      <p class="contact-line" style="top:14px"><strong>Khalid</strong> Bin Rashed</p>
      <p class="contact-line" style="top:55px">Managing Director</p>
      <div class="rule" style="top:102px"></div>

      <svg class="icon" style="top:146px" viewBox="0 0 40 40" aria-hidden="true">
        <path d="M2 14 C2 6 38 6 38 14 L38 18 L29 18 L29 13 L11 13 L11 18 L2 18 Z"/>
        <path d="M12 15 L28 15 L35 34 L5 34 Z"/>
        <circle cx="20" cy="25" r="5" fill="var(--panel-grey)"/>
      </svg>
      <p class="contact-line contact-line--small" style="top:124px">Office Tel +971 4 000 3829</p>
      <p class="contact-line contact-line--small" style="top:172px">Mobile +971 50 000 4172</p>
      <div class="rule" style="top:221px"></div>

      <svg class="icon" style="top:236px" viewBox="0 0 40 40" aria-hidden="true">
        <rect x="2" y="6" width="36" height="28" fill="none" stroke="var(--on-dark)" stroke-width="2"/>
        <path d="M2 6 L20 22 L38 6 M2 34 L15 20 M38 34 L25 20" fill="none" stroke="var(--on-dark)" stroke-width="2"/>
      </svg>
      <p class="contact-line" style="top:242px">khalid@corvane-example.ae</p>
      <div class="rule" style="top:294px"></div>

      <svg class="icon" style="top:306px" viewBox="0 0 40 40" aria-hidden="true">
        <g fill="none" stroke="var(--on-dark)" stroke-width="2.5">
          <circle cx="20" cy="20" r="17"/>
          <ellipse cx="20" cy="20" rx="7" ry="17"/>
          <path d="M3 20 H37 M6 11 H34 M6 29 H34"/>
        </g>
      </svg>
      <p class="contact-line" style="top:313px">www.corvane-example.ae</p>
      <div class="rule" style="top:359px"></div>

      <svg class="icon" style="top:378px" viewBox="0 0 40 40" aria-hidden="true">
        <path d="M20 2 C11 2 6 9 6 15 C6 25 20 38 20 38 C20 38 34 25 34 15 C34 9 29 2 20 2 Z"/>
        <circle cx="20" cy="15" r="5" fill="var(--panel-grey)"/>
      </svg>
      <p class="contact-line contact-line--small" style="top:381px">Palm Crest Tower, officw 18-B07,</p>
      <p class="contact-line contact-line--small" style="top:415px">Qasr Gardens, Dubai</p>
    </div>
  </section>

  <section class="card card--back" aria-label="Card back">
    <p class="services">Your services description here</p>
    <div class="brand brand--back">
      <span class="brand__name">CORVANE</span>
      <span class="brand__sub">HOLDINGS</span>
    </div>
  </section>
</body>
</html>
```